Updated web design for software design firm supporting entrepreneurs

Looking for a more modern looking, mobile friendly website design for our company, Brainwave2Binaries. B2B is a software development firm who supports people who have ideas for software and want to make them a reality. It also provides some maintenance work on existing websites as well as mobile apps. Please see our current website, www.brainwave2binaries-example.com, for more information on our business.

Old logo files included for reference. However, we are hoping to incorporate a new logo.

Like a blue'ish theme, but open to ideas.

Industry/Entity Type

Software

Logo Text

B2B and/or Brainwave2Binaries

Number of Pages Required

2 page

Font styles to use
Serif
Sans Serif

Colors
33a6d7
0255a3

Requirements
Must have
• Looking for 2 pages designed: 1 landing page and 1 type of secondary content page
• Please prepare menu for about 7 pages
Nice to have
• This will be implemented as a WordPress theme.
• Could include post-it note, white board, napkins, etc.

```html
<!DOCTYPE html>
<html lang="en">
<head>
<meta charset="utf-8">
<title>Brainwave2Binaries</title>
<link rel="stylesheet" href="https://fonts.googleapis.com/css2?family=Raleway:wght@400;500;600&family=Open+Sans:wght@400;600;700&display=swap">
<style>
:root{
  --blue:#0255a3;
  --sky:#33a6d7;
  --hero-box:rgba(2,85,163,.72);
  --ink:#222;
  --muted:#999;
  --bar:#3a3a3a;
  --dark:#1c1c1c;
  --card:#f2f2f2;
  --grey-band:#e1e1e1;
  --white:#fff;
}
*{margin:0;padding:0;box-sizing:border-box}
html,body{width:1200px;height:2795px;overflow:hidden}
body{position:relative;font-family:"Open Sans",sans-serif;color:var(--ink);background:var(--white)}
.abs{position:absolute}
.topbar{left:0;top:0;width:1200px;height:37px;background:var(--bar)}
.social-top{right:38px;top:7px;display:flex;gap:10px}
.dot-icon{width:23px;height:23px;border:2px solid #fff;border-radius:50%}
.header{left:0;top:37px;width:1200px;height:155px;background:#fff}
.brand{left:60px;top:80px;display:flex;align-items:center;gap:14px}
.brand-mark{width:58px;height:58px;border-radius:50%;background:var(--blue)}
.brand-name{font-family:"Raleway",sans-serif;font-weight:600;font-size:66px;color:var(--blue);letter-spacing:2px}
.contact-item{top:70px;display:flex;align-items:center;gap:14px}
.contact-icon{width:44px;height:44px;border-radius:50%;background:var(--blue);display:flex;align-items:center;justify-content:center}
.contact-label{font-size:12px;color:#333}
.contact-value{font-size:13px;font-weight:700;color:#111;margin-top:2px}
.nav{top:143px;right:60px;display:flex;gap:38px;font-size:16px;color:var(--blue)}
.hero{left:0;top:192px;width:1200px;height:531px;background:linear-gradient(90deg,#e9eef2 0%,#d6dde3 45%,#8a8f92 70%,#2d2f31 100%)}
.hero-box{left:60px;top:369px;width:530px;height:291px;background:var(--hero-box);padding:42px 24px;color:#fff}
.hero-title{font-family:"Raleway",sans-serif;font-size:42px;font-weight:400}
.hero-sub{font-family:"Raleway",sans-serif;font-size:24px;line-height:1.7;margin-top:8px}
.btn{display:inline-block;background:var(--blue);color:#fff;font-size:17px;text-align:center}
.hero-btn{margin-top:30px;width:186px;height:48px;line-height:48px}
.section-title{left:0;width:1200px;text-align:center;font-family:"Raleway",sans-serif;font-size:46px;color:var(--ink)}
.section-title span{color:var(--blue)}
.about-text{left:186px;top:858px;width:828px;text-align:center;font-size:13px;line-height:27px;color:#333}
.about-btn{left:507px;top:1000px;width:186px;height:51px;line-height:51px}
.services{left:0;top:1118px;width:1200px;height:472px;background:radial-gradient(ellipse at 50% 45%,#4a3a2e 0%,#262626 45%,var(--dark) 80%)}
.service{top:1180px;width:330px;text-align:center;color:#fff}
.service h3{font-family:"Raleway",sans-serif;font-weight:500;font-size:22px}
.service svg{margin:26px auto 18px;display:block}
.service p{font-size:13.5px;line-height:28px}
.testi-card{top:1706px;width:512px;height:159px;background:var(--card);padding:30px 32px}
.quote{font-family:Georgia,serif;font-size:40px;font-weight:700;color:var(--blue);line-height:24px}
.testi-card p{font-size:12.5px;line-height:24px;color:var(--muted);margin-top:6px}
.person{top:1876px;display:flex;align-items:center;gap:20px}
.avatar{width:86px;height:86px;border-radius:50%;background:linear-gradient(#d8dde2,#b9c2ca)}
.person-name{font-size:18px;color:var(--blue)}
.person-role{font-size:11px;color:var(--muted);margin-top:2px}
.dots{left:575px;top:1999px;display:flex;gap:6px}
.dots i{width:10px;height:10px;border-radius:50%;background:#ccc;display:block}
.dots i.on{background:#fff;border:3px solid var(--blue)}
.news-band{left:410px;top:2115px;width:790px;height:139px;background:var(--grey-band)}
.news-label{left:60px;top:2150px;color:#fff}
.news-label small{font-family:"Raleway",sans-serif;font-size:16px;display:block}
.news-label strong{font-family:"Raleway",sans-serif;font-weight:400;font-size:46px;display:block;margin-top:6px}
.news-input{left:522px;top:2161px;width:445px;height:49px;border-radius:8px;background:#9a9a9a;color:#eee;font-size:13px;line-height:49px;padding-left:18px}
.news-submit{left:984px;top:2161px;width:156px;height:49px;border-radius:8px;background:#050505;color:#fff;font-weight:700;font-size:16px;line-height:49px;text-align:center}
.map{left:0;top:2304px;width:600px;height:444px;background:linear-gradient(135deg,#5c5e58,#3f423d 55%,#4b4d47)}
.contact-pane{left:600px;top:2304px;width:600px;height:444px;background:#000}
.footer-title{font-family:"Open Sans",sans-serif;font-size:40px;color:#fff;letter-spacing:1px}
.addr-list{left:60px;top:2454px;color:#fff;font-size:13px}
.addr-list div{display:flex;align-items:center;gap:22px;height:39px}
.follow{left:60px;top:2587px;color:#fff;font-size:18px}
.follow-icons{left:60px;top:2624px;display:flex;gap:14px}
.field{left:645px;width:447px;background:#fff;border-radius:9px;font-size:13px;color:#333;padding:10px 20px}
.send{left:990px;top:2684px;width:102px;height:41px;border-radius:9px;background:var(--sky);color:#fff;font-size:14px;line-height:41px;text-align:center}
.copyright{left:0;top:2748px;width:1200px;height:47px;background:var(--blue);color:#fff;font-size:12.5px;text-align:center;line-height:47px}
</style>
</head>
<body>

<div class="abs topbar"></div>
<div class="abs social-top"><span class="dot-icon"></span><span class="dot-icon"></span><span class="dot-icon"></span><span class="dot-icon"></span></div>

<header class="abs header"></header>
<div class="abs brand"><span class="brand-mark"></span><span class="brand-name">B2B</span></div>
<div class="abs contact-item" style="left:615px">
  <span class="contact-icon"><svg width="20" height="20" viewBox="0 0 24 24"><path fill="#fff" d="M6.6 10.8a15 15 0 0 0 6.6 6.6l2.2-2.2c.3-.3.7-.4 1-.2 1.1.4 2.3.6 3.6.6.6 0 1 .4 1 1V20c0 .6-.4 1-1 1C10.6 21 3 13.4 3 4c0-.6.4-1 1-1h3.5c.6 0 1 .4 1 1 0 1.3.2 2.5.6 3.6.1.3 0 .7-.2 1z"/></svg></span>
  <div><div class="contact-label">Contact Number</div><div class="contact-value">(555) 014-2387</div></div>
</div>
<div class="abs contact-item" style="left:848px">
  <span class="contact-icon"><svg width="22" height="16" viewBox="0 0 22 16"><rect x="1" y="1" width="20" height="14" rx="1" fill="#fff"/><path d="M1 1l10 8 10-8" stroke="#0255a3" stroke-width="1.6" fill="none"/></svg></span>
  <div><div class="contact-label">Contact Email</div><div class="contact-value">question@brainwave2binaries-example.com</div></div>
</div>
<nav class="abs nav"><span>Who We Are</span><span>how it Works</span><span>Who needs Us</span><span>Odd Jobs</span><span>Portfolio</span><span>Contact US</span></nav>

<section class="abs hero" role="img" aria-label="Photo of a businessman holding a young seedling in soil in cupped hands, bright office background"></section>
<div class="abs hero-box">
  <div class="hero-title">Brainwave2Binaries</div>
  <div class="hero-sub">can help anyone turn their software idea into reality.</div>
  <span class="btn hero-btn">Read More</span>
</div>

<h2 class="abs section-title" style="top:782px"><span>Who</span> We Are</h2>
<p class="abs about-text">Brainwave2Binaries can help anyone turn their software idea into reality. We understand that you don't have to be a big company to have big ideas, but turning those ideas into functional software can be time consuming, expensive and seem out of reach. Brainwave2Binaries specializes in helping small businesses and individuals take their idea from the back of a napkin to the desktop. As a small business ourselves, we understand the need to be flexible, efficient and cost-conscious. We'll take your idea from a vision in your head to a fully working system.</p>
<span class="abs btn about-btn"><svg width="16" height="14" viewBox="0 0 16 14" style="vertical-align:-2px;margin-right:14px"><path d="M1 7h13M9 2l5 5-5 5" stroke="#fff" stroke-width="2.2" fill="none"/></svg>Read More</span>

<section class="abs services" role="img" aria-label="Dark photo of hands holding soil with a small plant"></section>
<div class="abs service" style="left:75px">
  <h3>Social Networking</h3>
  <svg width="76" height="62" viewBox="0 0 76 62"><ellipse cx="30" cy="24" rx="28" ry="20" fill="#fff"/><path d="M14 38l-6 14 16-9z" fill="#fff"/><ellipse cx="50" cy="36" rx="22" ry="16" fill="#fff" stroke="#222" stroke-width="3"/><path d="M62 48l8 11-15-7z" fill="#fff"/></svg>
  <p>We have built a variety of social networking applications that were inspired by well known social media platforms such as Chatterly and Quiply. Whether it's connecting entrepreneurs, teams within organizations or families, we have the skills to build software that leverages and encourages these connections.</p>
</div>
<div class="abs service" style="left:435px">
  <h3>E-commerce</h3>
  <svg width="76" height="62" viewBox="0 0 76 62"><circle cx="30" cy="30" r="27" fill="#fff"/><g stroke="#222" stroke-width="2.5" fill="none"><ellipse cx="30" cy="30" rx="11" ry="27"/><path d="M3 30h54M7 16h46M7 44h46"/></g><path d="M38 34h6l5 16h18l4-12H46" stroke="#fff" stroke-width="5" fill="#222"/><circle cx="52" cy="57" r="3.5" fill="#fff"/><circle cx="64" cy="57" r="3.5" fill="#fff"/></svg>
  <p>We've worked with organizations selling everything from children's bedding to the licensing of theater productions. Some of the cart solutions we've worked with include CartForge, ShopRiver, SellBox, StoreCraft, not to mention PayWell integration. We've also implemented custom shopping cart solutions</p>
</div>
<div class="abs service" style="left:795px">
  <h3>Mapping Software</h3>
  <svg width="76" height="62" viewBox="0 0 76 62"><circle cx="38" cy="31" r="29" fill="#fff"/><g stroke="#222" stroke-width="3" fill="none"><ellipse cx="38" cy="31" rx="12" ry="29"/><path d="M9 31h58M38 2v58"/></g></svg>
  <p>Brainwave2Binaries has made extensive use of the MapGrid API, including interactive custom mapping applications as well as implementing custom map tiles. We've built software that manages very large POI databases and used sophisticated geographic based searching and filtering.</p>
</div>

<h2 class="abs section-title" style="top:1615px"><span>Client</span> Testimonials</h2>
<div class="abs testi-card" style="left:60px"><div class="quote">&ldquo;</div><p>The customer support that this website has provided me with is as close to perfect as I've seen. Their responses were fast and helpful as the same time. Great job guys!</p></div>
<div class="abs testi-card" style="left:600px"><div class="quote">&ldquo;</div><p>The customer support that this website has provided me with is as close to perfect as I've seen. Their responses were fast and helpful as the same time. Great job guys!</p></div>
<div class="abs person" style="left:92px"><span class="avatar" role="img" aria-label="Client portrait"></span><div><div class="person-name">Marta Linwood</div><div class="person-role">CEO &amp; Founder NOVA</div></div></div>
<div class="abs person" style="left:632px"><span class="avatar" role="img" aria-label="Client portrait"></span><div><div class="person-name">Marta Linwood</div><div class="person-role">CEO &amp; Founder NOVA</div></div></div>
<div class="abs dots"><i class="on"></i><i></i><i></i></div>

<div class="abs news-band"></div>
<svg class="abs" style="left:0;top:2068px" width="512" height="236" viewBox="0 0 512 236"><path d="M0 0H410L512 236H0z" fill="#0255a3"/></svg>
<div class="abs news-label"><small>Sing-up for</small><strong>The Newsletter</strong></div>
<div class="abs news-input">Enter your E-mail Address</div>
<div class="abs news-submit">SUBMIT</div>

<section class="abs map" role="img" aria-label="Dimmed regional road map"></section>
<div class="abs contact-pane"></div>
<h3 class="abs footer-title" style="left:60px;top:2376px">ADDRESS HERE</h3>
<div class="abs addr-list">
  <div><svg width="14" height="20" viewBox="0 0 14 20"><path d="M7 0a7 7 0 0 1 7 7c0 5-7 13-7 13S0 12 0 7a7 7 0 0 1 7-7z" fill="#fff"/><circle cx="7" cy="7" r="2.6" fill="#444"/></svg>Northfield Valley, USA.</div>
  <div><svg width="16" height="16" viewBox="0 0 24 24"><path fill="#fff" d="M6.6 10.8a15 15 0 0 0 6.6 6.6l2.2-2.2c.3-.3.7-.4 1-.2 1.1.4 2.3.6 3.6.6.6 0 1 .4 1 1V20c0 .6-.4 1-1 1C10.6 21 3 13.4 3 4c0-.6.4-1 1-1h3.5c.6 0 1 .4 1 1 0 1.3.2 2.5.6 3.6.1.3 0 .7-.2 1z"/></svg>(555) 014-2387</div>
  <div><svg width="18" height="13" viewBox="0 0 22 16"><rect x="1" y="1" width="20" height="14" fill="#fff"/><path d="M1 1l10 8 10-8" stroke="#444" stroke-width="1.6" fill="none"/></svg>questions@brainwave2binaries-example.com</div>
</div>
<div class="abs follow">Follow us</div>
<div class="abs follow-icons"><span class="dot-icon"></span><span class="dot-icon"></span><span class="dot-icon"></span><span class="dot-icon"></span><span class="dot-icon"></span></div>

<h3 class="abs footer-title" style="left:645px;top:2376px">CONTACT US</h3>
<div class="abs field" style="top:2440px;height:41px">Your Name (required)</div>
<div class="abs field" style="top:2496px;height:41px">Your Email (required)</div>
<div class="abs field" style="top:2552px;height:105px">How can we help?</div>
<div class="abs send">SEND</div>

<footer class="abs copyright">Copyright © 2017 www.brainwave2binaries-example.com. All Right Reserved.</footer>

</body>
</html>
```